Calderwyn Structural Roof Inc.

We need a business card design for a commercial roofing company metro Boston based. We are a roofing company that help people manage buildings and build relationships with clients. We would like a unique card that stands out. We want a business card with a white background. We do not want a roof as the logo.

Industry/Entity Type

Roofing

```html
<!DOCTYPE html>
<html lang="en">
<head>
<meta charset="UTF-8">
<title>Calderwyn Structural Roof Inc. — Business Card</title>
<link rel="stylesheet" href="https://fonts.googleapis.com/css2?family=Open+Sans:ital,wght@0,400;0,600;0,800;1,400;1,800&display=swap">
<style>
  :root {
    --page-bg: #e9e9eb;
    --card-bg: #ffffff;
    --brand-blue: #2a6fb5;
    --deep-blue: #1f4fa0;
    --sky-blue: #2f9ad8;
    --text-grey: #5d6168;
    --band-grey: #9aa2ad;
  }
  * { box-sizing: border-box; margin: 0; padding: 0; }
  html, body {
    width: 1200px; height: 900px; overflow: hidden;
    background: var(--page-bg);
    font-family: "Open Sans", Arial, sans-serif;
  }
  .card {
    position: absolute; left: 100px; top: 164px;
    width: 1000px; height: 572px;
    background: var(--card-bg);
    box-shadow: 0 6px 24px rgba(0,0,0,0.12);
    overflow: hidden;
  }
  .brand {
    position: absolute; top: 108px; left: 0; width: 100%;
    display: flex; justify-content: center; align-items: center; gap: 18px;
  }
  .brand-mark { width: 30px; height: 30px; background: var(--brand-blue); }
  .brand-name { font-size: 36px; font-weight: 600; color: var(--brand-blue); letter-spacing: 1px; }
  .holder { position: absolute; left: 60px; top: 222px; }
  .holder-name {
    font-size: 30px; font-weight: 800; font-style: italic;
    color: var(--deep-blue); text-transform: uppercase; letter-spacing: 0.5px;
  }
  .holder-role { font-size: 23px; font-style: italic; color: var(--text-grey); margin-top: 2px; }
  .divider {
    position: absolute; left: 0; top: 310px; width: 970px; height: 5px;
    background: linear-gradient(90deg, var(--sky-blue), var(--deep-blue));
  }
  .contact-left { position: absolute; left: 60px; top: 340px; color: var(--text-grey); font-size: 22px; font-style: italic; }
  .contact-left .line { display: flex; align-items: center; gap: 12px; height: 40px; }
  .contact-right { position: absolute; left: 530px; top: 380px; color: var(--text-grey); font-size: 22px; font-weight: 600; letter-spacing: 1px; }
  .contact-right .line { display: flex; align-items: center; gap: 22px; height: 48px; }
  .icon { width: 26px; height: 26px; flex: none; }
  .bands { position: absolute; left: 0; bottom: 0; width: 1000px; height: 80px; }
</style>
</head>
<body>
  <div class="card">
    <div class="brand">
      <span class="brand-mark"></span>
      <span class="brand-name">Calderwyn Structural Roof Inc.</span>
    </div>

    <div class="holder">
      <div class="holder-name">Marcus Ellery</div>
      <div class="holder-role">President</div>
    </div>

    <div class="divider"></div>

    <div class="contact-left">
      <div class="line">Your Address Goes Here</div>
      <div class="line">
        <svg class="icon" viewBox="0 0 26 26" aria-hidden="true">
          <rect x="7" y="2" width="12" height="22" rx="2" fill="var(--deep-blue)"/>
          <rect x="9" y="5" width="8" height="8" fill="#fff"/>
        </svg>
        (617) 555-0142
      </div>
    </div>

    <div class="contact-right">
      <div class="line">
        <svg class="icon" viewBox="0 0 26 26" aria-hidden="true">
          <rect x="2" y="5" width="22" height="16" fill="none" stroke="var(--deep-blue)" stroke-width="2"/>
          <path d="M2 5 L13 14 L24 5" fill="none" stroke="var(--deep-blue)" stroke-width="2"/>
        </svg>
        www.yourwebsite.com
      </div>
      <div class="line">
        <svg class="icon" viewBox="0 0 26 26" aria-hidden="true">
          <circle cx="13" cy="13" r="10" fill="none" stroke="var(--deep-blue)" stroke-width="2"/>
          <ellipse cx="13" cy="13" rx="4.5" ry="10" fill="none" stroke="var(--deep-blue)" stroke-width="2"/>
          <line x1="3" y1="13" x2="23" y2="13" stroke="var(--deep-blue)" stroke-width="2"/>
        </svg>
        email@provider.com
      </div>
    </div>

    <svg class="bands" viewBox="0 0 1000 80" preserveAspectRatio="none" aria-hidden="true">
      <defs>
        <linearGradient id="blueBand" x1="0" x2="1" y1="0" y2="0">
          <stop offset="0" stop-color="#2f9ad8"/>
          <stop offset="1" stop-color="#1f4fa0"/>
        </linearGradient>
      </defs>
      <polygon points="0,22 490,22 460,48 0,48" fill="var(--band-grey)"/>
      <polygon points="440,80 490,40 1000,30 1000,80" fill="url(#blueBand)"/>
    </svg>
  </div>
</body>
</html>
```